Website Design For our Tour Company

We need a face lift on our current website. I want it to look the best! Lots of videos. An easy to use website to obtain easy conversions. I want people to feel like they are on the tour just by looking at our website. My current website is just bland and unprofessional looking. I want it to be incredibly mobile friendly and look great on the desk top. Our current website is https://www.kellbrookvoyages.example/
I would like there to be an option where the viewer can select what language they would like to read in. Im hoping you can pull a-lot of media and videos from out facebook page. Im not happy with most of my descriptions for the product and tours we offer. Looking for professional help.

Our two main activities are Summer and Winter Tours
In The Summer the main things we do our Jet Boat & Jet Ski Tours.

In The Winter our main tour is luxury first class Aurora Viewing. I Would like to see a-lot of aurora video/photos as I believe that gets peoples attention!

Target Market(s)

Travelers from china and around the world

Coding

Coded - Design and coding required

Number of Pages Required

5+ page

Requirements
Must have
• be able to select what when language you would like to read the website in.
Nice to have
• The overall look and feel I want for the website is luxury, fancy, royalty. Think Gerald Mossworth. I like the Luxury gold colors. I need the website to look ridiculously professional

incorporate Lots of Aurora photos / videos as one of our main tours is Aurora

```html
<!DOCTYPE html>
<html lang="en">
<head>
<meta charset="utf-8">
<title>Kellbrook Voyages</title>
<link rel="stylesheet" href="https://fonts.googleapis.com/css2?family=Cormorant+Garamond:wght@600;700&family=Yellowtail&family=Nunito+Sans:wght@400;600;700&family=Poppins:wght@400;500;600&display=swap">
<style>
:root{
  --gold:#c9970f;
  --gold-light:#e6b93a;
  --gold-dark:#a87a06;
  --tan:#c39a52;
  --paper:#f4f2ef;
  --ink:#3a3a3a;
  --muted:#555;
  --footer:#3d2b0c;
  --footer-deep:#33240a;
  --white:#ffffff;
}
*{box-sizing:border-box;margin:0;padding:0}
html,body{width:1200px;height:3621px;overflow:hidden}
body{position:relative;background:var(--paper);font-family:"Nunito Sans",sans-serif;color:var(--ink)}
.abs{position:absolute}
.photo{position:absolute}

/* Hero */
.hero{left:0;top:0;width:1200px;height:720px}
.hero-bg{left:0;top:0;width:1200px;height:720px;background:linear-gradient(180deg,#2f4a86 0%,#39588f 22%,#2a3c55 34%,#1c2a3c 44%,#2d4a78 60%,#22355e 100%)}
.brand{left:100px;top:30px;display:flex;align-items:center;gap:10px;white-space:nowrap}
.brand-dot{width:40px;height:40px;border-radius:50%;border:2px solid var(--gold-light);flex:none}
.brand-name{font-family:"Cormorant Garamond",serif;font-weight:700;font-size:23px;color:var(--gold-light);letter-spacing:1px;line-height:1}
.nav-link{position:absolute;top:54px;font-family:"Nunito Sans",sans-serif;font-size:17px;line-height:24px;color:var(--white);text-decoration:none;white-space:nowrap}
.nav-link.active{color:var(--gold-light)}
.lang{left:992px;top:50px;width:112px;height:32px;border:1px solid rgba(255,255,255,.45);color:#fff;font-size:14px;display:flex;align-items:center;justify-content:space-between;padding:0 14px}
.hero-title{left:0;width:1200px;top:250px;text-align:center;color:#fff}
.hero-script{font-family:"Yellowtail",cursive;font-size:96px;line-height:1}
.hero-name{font-family:"Cormorant Garamond",serif;font-weight:600;font-size:46px;margin-top:10px}
.hero-tag{font-size:17px;margin-top:8px}

/* Section headings */
.heading{width:1200px;left:0;text-align:center}
.heading h2{font-family:"Cormorant Garamond",serif;font-weight:700;font-size:46px;color:var(--gold);line-height:1}
.rule{display:block;margin:10px auto 0}

/* About */
.about-photo{left:225px;top:850px;width:245px;height:300px}
.about-text{left:638px;top:876px;width:480px;font-size:15px;color:var(--muted);line-height:1.6}
.about-text h3{font-size:18px;font-weight:700;color:#333;margin-bottom:12px}
.about-text ul{list-style:none;margin-top:12px}
.about-text li{position:relative;padding-left:32px;margin-bottom:16px}
.about-text li::before{content:"";position:absolute;left:2px;top:10px;width:20px;height:3px;border-radius:2px;background:var(--gold)}
.btn{display:inline-flex;align-items:center;justify-content:center;gap:8px;background:linear-gradient(180deg,var(--gold-light),var(--gold-dark));color:#fff;font-size:15px;font-family:"Nunito Sans",sans-serif;white-space:nowrap}
.learn{left:643px;top:1172px;width:148px;height:44px}

/* Deals */
.deals-bg{left:0;top:1360px;width:1200px;height:520px;background:linear-gradient(90deg,#d9d9d9 0%,#ececec 35%,#f3f3f3 55%,#d6d6d6 80%,#c9c9c9 100%)}
.shield-title{font-family:"Cormorant Garamond",serif;font-weight:700;font-size:38px;color:var(--gold);text-align:center;line-height:1.1}
.shield-sub{font-size:16px;color:#222;text-align:center;line-height:1.5;margin-top:20px}
.deal-btn{width:170px;height:40px;top:1734px}
.center-deal{left:440px;top:1566px;width:320px;text-align:center}
.center-deal h2{font-family:"Cormorant Garamond",serif;font-weight:700;font-size:38px;color:var(--gold);line-height:1.2}

/* Gallery */
.gallery-bg{left:0;top:1880px;width:1200px;height:890px;background:linear-gradient(180deg,#4f5784 0%,#6c74a0 30%,#8d8fb0 50%,#4d5a4f 70%,#2f3e60 85%,#1f2f55 100%)}
.gallery-photo{left:156px;top:2113px;width:856px;height:535px;background:radial-gradient(ellipse at 50% 55%,#e08a2a 0%,#b8621a 14%,#3d4a68 34%,#2d3b54 60%,#3c4a2a 100%)}
.dots{left:555px;top:2682px;display:flex;gap:8px}
.dots span{width:11px;height:11px;border-radius:50%;border:1px solid #fff}
.dots span.on{width:16px;height:16px;margin-top:-2px;background:#fff;box-shadow:inset 0 0 0 3px #6d7aa0}

/* Contact */
.form{left:413px;top:2914px;width:374px}
.field{width:374px;height:32px;border:1px solid var(--gold);background:#fff;font-size:14px;color:#666;padding:6px 15px;margin-bottom:10px}
.field.message{height:82px}
.submit{left:538px;top:3138px;width:124px;height:40px;font-weight:700}

/* Footer */
.footer-bg{left:0;top:3260px;width:1200px;height:361px}
.foot-brand{left:130px;top:3378px;width:160px;text-align:center}
.foot-circle{width:90px;height:90px;border-radius:50%;border:2px solid var(--tan);margin:0 auto 12px}
.foot-name{font-family:"Poppins",sans-serif;font-weight:500;font-size:17px;color:var(--tan);white-space:nowrap}
.socials{display:flex;gap:22px;justify-content:center;margin-top:14px}
.socials span{width:14px;height:14px;border-radius:50%;background:var(--gold)}
.foot-col{font-family:"Poppins",sans-serif;color:#f1e7d2}
.foot-col h4{font-size:15px;font-weight:600;margin-bottom:18px}
.foot-col p,.foot-col li{font-size:12.5px;line-height:1.8}
.foot-col ul{list-style:none}
.contact-row{display:flex;gap:14px;align-items:flex-start;margin-bottom:14px}
.contact-row svg{flex:none;margin-top:3px}
.foot-call{left:840px;top:3463px;width:176px;height:46px;border-radius:24px;background:linear-gradient(180deg,var(--gold-light),var(--gold-dark));color:#fff;font-family:"Poppins",sans-serif;font-size:17px;display:flex;align-items:center;gap:10px;padding-left:2px}
.call-icon{width:44px;height:44px;border-radius:50%;background:#111;display:flex;align-items:center;justify-content:center;border:2px solid var(--gold-light)}
.bottom-line{left:0;top:3556px;width:1200px;height:1px;background:rgba(255,255,255,.18)}
.copyright{left:120px;top:3580px;font-family:"Poppins",sans-serif;font-size:13px;color:#e9dcc0}
.legal{left:872px;top:3580px;font-family:"Poppins",sans-serif;font-size:12.5px;color:#e9dcc0}
</style>
</head>
<body>

<!-- Hero -->
<section class="abs hero">
  <div class="photo hero-bg" role="img" aria-label="Two smiling riders on a red jet ski on a calm northern lake at dusk, with spruce forest and docks behind"></div>
  <div class="abs brand">
    <span class="brand-dot"></span>
    <span class="brand-name">KELLBROOK VOYAGES</span>
  </div>
  <nav>
    <a class="nav-link active" style="left:484px" href="#">Home</a>
    <a class="nav-link" style="left:563px" href="#">Summer Tours</a>
    <a class="nav-link" style="left:720px" href="#">Winter Tours</a>
    <a class="nav-link" style="left:864px" href="#">Book Online</a>
  </nav>
  <div class="abs lang"><span>English</span>
    <svg width="14" height="8" viewBox="0 0 14 8"><path d="M1 1l6 6 6-6" fill="none" stroke="#fff" stroke-width="1.3"/></svg>
  </div>
  <div class="abs hero-title">
    <div class="hero-script">Welcome To</div>
    <div class="hero-name">Kellbrook Voyages</div>
    <div class="hero-tag">Taking You Where You Want To Go</div>
  </div>
  <svg class="abs" style="left:581px;top:594px" width="38" height="14" viewBox="0 0 38 14"><path d="M1 1l18 11 18-11" fill="none" stroke="#fff" stroke-width="1.6"/></svg>
  <svg class="abs" style="left:0;top:560px" width="1200" height="170" viewBox="0 0 1200 170">
    <path d="M0 140 C 200 140 320 95 520 95 C 760 95 900 10 1200 10 L1200 170 L0 170 Z" fill="var(--paper)"/>
    <path d="M0 140 C 200 140 320 95 520 95 C 760 95 900 10 1200 10" fill="none" stroke="var(--gold)" stroke-width="5"/>
  </svg>
</section>

<!-- About -->
<div class="abs heading" style="top:755px">
  <h2>About Us</h2>
  <svg class="rule" width="212" height="14" viewBox="0 0 212 14"><line x1="0" y1="7" x2="80" y2="7" stroke="var(--gold)" stroke-width="1"/><circle cx="106" cy="7" r="4" fill="var(--gold)"/><line x1="132" y1="7" x2="212" y2="7" stroke="var(--gold)" stroke-width="1"/></svg>
</div>
<svg class="photo about-photo" viewBox="0 0 245 300" role="img" aria-label="Guide standing beside a jet ski on a river dock with a paddlewheel riverboat behind">
  <defs><linearGradient id="aboutFill" x1="0" y1="0" x2="0" y2="1"><stop offset="0" stop-color="#6d8a6a"/><stop offset=".5" stop-color="#4e5e6e"/><stop offset="1" stop-color="#2c3644"/></linearGradient></defs>
  <path d="M122 0 L245 60 L235 205 Q122 300 10 205 L0 60 Z" fill="url(#aboutFill)"/>
</svg>
<div class="abs about-text">
  <h3>Great Journeys. Fascinating Places.</h3>
  <p>Local Experts Ryan, Elena, and Colby</p>
  <ul>
    <li>Colby - Life-long Alaskan - Local expert, loves the outdoors, construction, &amp; adventures</li>
    <li>Ryan - Life-long Alaskan - Local expert entrepreneur, loves Alaska, always ready for an adventure and a fun time!</li>
    <li>Elena - Life-long Alaska - Local expert, company cook, organizes the activities &amp; schedule. Without her we have no organization.</li>
  </ul>
</div>
<a class="abs btn learn">Learn More
  <svg width="15" height="15" viewBox="0 0 15 15"><circle cx="7.5" cy="7.5" r="7" fill="#fff"/><path d="M6 4.5l3 3-3 3" fill="none" stroke="var(--gold)" stroke-width="1.6"/></svg>
</a>

<!-- Deals -->
<div class="photo deals-bg" role="img" aria-label="Faded split scene of kayaks on a summer lake and snowshoe hikers in a winter forest"></div>
<svg class="abs" style="left:0;top:1340px" width="1200" height="80" viewBox="0 0 1200 80">
  <path d="M0 0 L1200 0 L1200 66 C 950 20 700 20 450 20 C 260 20 150 30 0 50 Z" fill="var(--paper)"/>
  <path d="M0 50 C 150 30 260 20 450 20 C 700 20 950 70 1200 66" fill="none" stroke="var(--gold)" stroke-width="5"/>
</svg>
<svg class="abs" style="left:0;top:1842px" width="1200" height="80" viewBox="0 0 1200 80">
  <path d="M0 18 C 250 0 450 5 650 30 C 850 52 1000 35 1200 12 L1200 80 L0 80 Z" fill="#555e86"/>
  <path d="M0 18 C 250 0 450 5 650 30 C 850 52 1000 35 1200 12" fill="none" stroke="var(--gold)" stroke-width="5"/>
</svg>
<svg class="abs" style="left:172px;top:1462px" width="266" height="280" viewBox="0 0 266 280">
  <path d="M133 6 L260 70 Q268 190 210 272 M56 272 Q-2 190 6 70 L133 6" fill="none" stroke="var(--tan)" stroke-width="12"/>
</svg>
<svg class="abs" style="left:776px;top:1462px" width="266" height="280" viewBox="0 0 266 280">
  <path d="M133 6 L260 70 Q268 190 210 272 M56 272 Q-2 190 6 70 L133 6" fill="none" stroke="var(--tan)" stroke-width="12"/>
</svg>
<div class="abs" style="left:175px;top:1545px;width:260px">
  <div class="shield-title">Summer<br>Tours</div>
  <div class="shield-sub">Land Of The<br>Midnight Sun</div>
</div>
<div class="abs" style="left:778px;top:1545px;width:260px">
  <div class="shield-title">Winter<br>Tours</div>
  <div class="shield-sub">Explore The Winter<br>Wonderland</div>
</div>
<a class="abs btn deal-btn" style="left:220px">Begin Adventure</a>
<a class="abs btn deal-btn" style="left:823px">Begin Adventure</a>
<div class="abs center-deal">
  <h2>Great Deals<br>On Guided Tours</h2>
  <svg class="rule" width="212" height="14" viewBox="0 0 212 14"><line x1="0" y1="7" x2="80" y2="7" stroke="var(--gold)" stroke-width="1"/><circle cx="106" cy="7" r="4" fill="var(--gold)"/><line x1="132" y1="7" x2="212" y2="7" stroke="var(--gold)" stroke-width="1"/></svg>
</div>

<!-- Gallery -->
<div class="photo gallery-bg" role="img" aria-label="Kayakers paddling across a wide river under a cloudy evening sky"></div>
<svg class="abs" style="left:0;top:1842px" width="1200" height="60" viewBox="0 0 1200 60">
  <path d="M0 18 C 250 0 450 5 650 30 C 850 52 1000 35 1200 12" fill="none" stroke="var(--gold)" stroke-width="5"/>
</svg>
<div class="abs heading" style="top:1978px">
  <h2 style="color:#fff">Gallery</h2>
  <svg class="rule" width="212" height="14" viewBox="0 0 212 14"><line x1="0" y1="7" x2="80" y2="7" stroke="#fff" stroke-width="1"/><circle cx="106" cy="7" r="4" fill="#fff"/><line x1="132" y1="7" x2="212" y2="7" stroke="#fff" stroke-width="1"/></svg>
</div>
<svg class="abs" style="left:168px;top:2076px" width="880" height="554" viewBox="0 0 880 554">
  <path d="M20 26 V2 H878 V552 H860" fill="none" stroke="var(--gold-light)" stroke-width="3"/>
  <path d="M2 44 V20 H860 V534 H844" fill="none" stroke="var(--gold-light)" stroke-width="3"/>
</svg>
<div class="photo gallery-photo" role="img" aria-label="Smiling paddler in a red life vest sitting in a yellow kayak on a calm river, holding a paddle"></div>
<div class="abs dots"><span></span><span class="on"></span><span></span><span></span><span></span></div>

<!-- Contact -->
<div class="abs heading" style="top:2826px">
  <h2>About Us</h2>
  <svg class="rule" width="212" height="14" viewBox="0 0 212 14"><line x1="0" y1="7" x2="80" y2="7" stroke="var(--gold)" stroke-width="1"/><circle cx="106" cy="7" r="4" fill="var(--gold)"/><line x1="132" y1="7" x2="212" y2="7" stroke="var(--gold)" stroke-width="1"/></svg>
</div>
<form class="abs form">
  <div class="field">Name</div>
  <div class="field">Email</div>
  <div class="field">Subject</div>
  <div class="field message">Message</div>
</form>
<a class="abs btn submit">Submit</a>

<!-- Footer -->
<svg class="abs footer-bg" viewBox="0 0 1200 361">
  <defs><linearGradient id="footFill" x1="0" y1="0" x2="0" y2="1"><stop offset="0" stop-color="var(--footer)"/><stop offset="1" stop-color="var(--footer-deep)"/></linearGradient></defs>
  <path d="M0 22 C 200 28 400 40 640 38 C 880 36 1050 20 1200 0 L1200 361 L0 361 Z" fill="url(#footFill)"/>
  <path d="M0 22 C 200 28 400 40 640 38 C 880 36 1050 20 1200 0" fill="none" stroke="var(--gold)" stroke-width="4"/>
</svg>
<div class="abs foot-brand">
  <div class="foot-circle"></div>
  <div class="foot-name">Kellbrook Voyages</div>
  <div class="socials"><span></span><span></span><span></span></div>
</div>
<div class="abs foot-col" style="left:373px;top:3350px;width:240px">
  <h4>Contact Us</h4>
  <div class="contact-row">
    <svg width="14" height="18" viewBox="0 0 14 18"><path d="M7 17s6-6.5 6-10.5A6 6 0 0 0 1 6.5C1 10.5 7 17 7 17z" fill="none" stroke="#f1e7d2" stroke-width="1.3"/><circle cx="7" cy="6.5" r="2" fill="none" stroke="#f1e7d2" stroke-width="1.3"/></svg>
    <p>42 Birchline Road #4<br>Larchmont 99801 AK</p>
  </div>
  <div class="contact-row">
    <svg width="16" height="16" viewBox="0 0 16 16"><path d="M3 1l3 3-2 2c1 2.5 3.5 5 6 6l2-2 3 3-2 2C7 14 2 9 1 3z" fill="#f1e7d2"/></svg>
    <p>555.014.2290</p>
  </div>
  <div class="contact-row">
    <svg width="16" height="12" viewBox="0 0 16 12"><rect x=".7" y=".7" width="14.6" height="10.6" fill="none" stroke="#f1e7d2" stroke-width="1.3"/><path d="M1 1l7 6 7-6" fill="none" stroke="#f1e7d2" stroke-width="1.3"/></svg>
    <p>info@kellbrookvoyages.example</p>
  </div>
</div>
<div class="abs foot-col" style="left:643px;top:3350px;width:140px">
  <h4>Company</h4>
  <ul><li>Home</li><li>Vineyard</li><li>Wines</li><li>Press</li><li>Contact Us</li></ul>
</div>
<div class="abs foot-col" style="left:840px;top:3350px;width:240px">
  <h4>Stil have questions?</h4>
  <p>A representative will aswer your questions as soon as possible.</p>
</div>
<div class="abs foot-call">
  <span class="call-icon"><svg width="20" height="20" viewBox="0 0 16 16"><path d="M3 1l3 3-2 2c1 2.5 3.5 5 6 6l2-2 3 3-2 2C7 14 2 9 1 3z" fill="none" stroke="#fff" stroke-width="1.2"/></svg></span>
  555.014.2290
</div>
<div class="abs bottom-line"></div>
<div class="abs copyright">Copyright 2020 Kellbrook Voyages. All Rights Reserved.</div>
<div class="abs legal">Privacy Policy &nbsp;|&nbsp; Terms Of Services</div>

</body>
</html>
```